Need a professional card design. Marlowe building company specialise in residential and commercial builds. New homes, additions & renovations.
Wanting a card with creativity and professionalism.
Want card that utilises logo.

Back and front.

I have just created a logo, and want to use it on the business card.
Attached a copy of the logo.
Attached is also a current business card which I wish to redesign

please utilise both sides

• Reg# 38095

```html
<!DOCTYPE html>
<html lang="en">
<head>
<meta charset="utf-8">
<title>Marlowe Building Co – Business Card</title>
<link href="https://fonts.googleapis.com/css2?family=Open+Sans:wght@400;600&display=swap" rel="stylesheet">
<style>
  :root {
    --stage: #2b2b2d;
    --navy: #111521;
    --ink: #1c1f26;
    --gold: #e39b2e;
    --gold-deep: #c98421;
    --white: #ffffff;
    --paper: #f7f7f7;
  }
  * { box-sizing: border-box; margin: 0; padding: 0; }
  html, body { width: 1200px; height: 900px; overflow: hidden; }
  body {
    background: var(--stage);
    font-family: "Open Sans", Arial, sans-serif;
    display: flex;
    flex-direction: column;
    align-items: center;
    justify-content: center;
    gap: 46px;
  }
  .card {
    position: relative;
    width: 660px;
    height: 377px;
    border-radius: 22px;
    overflow: hidden;
  }

  /* Back side */
  .card-back {
    background: var(--navy);
    display: flex;
    flex-direction: column;
    align-items: center;
    justify-content: center;
    gap: 22px;
  }
  .wordmark {
    display: flex;
    align-items: center;
    gap: 14px;
    font-weight: 600;
    letter-spacing: 0.04em;
  }
  .wordmark-mark {
    width: 14px;
    height: 14px;
    background: var(--gold);
  }
  .card-back .wordmark { color: var(--white); font-size: 40px; }
  .card-back .wordmark-mark { width: 18px; height: 18px; }
  .tagline {
    color: var(--gold);
    font-size: 19px;
    font-weight: 600;
    text-align: center;
    line-height: 1.45;
  }

  /* Front side */
  .card-front { background: var(--paper); }
  .front-wave { position: absolute; inset: 0; }
  .front-wordmark {
    position: absolute;
    left: 44px;
    top: 108px;
    color: var(--ink);
    font-size: 29px;
  }
  .reg {
    position: absolute;
    right: 40px;
    top: 30px;
    font-size: 11px;
    color: var(--ink);
  }
  .person {
    position: absolute;
    right: 40px;
    top: 96px;
    text-align: right;
  }
  .person-name { color: var(--gold); font-size: 21px; font-weight: 600; }
  .person-role { color: var(--ink); font-size: 15px; font-weight: 600; margin-top: -2px; }
  .contacts {
    position: absolute;
    right: 40px;
    top: 190px;
    text-align: right;
    color: var(--ink);
    font-size: 16px;
    line-height: 1.5;
  }
  .contact-line { display: flex; justify-content: flex-end; align-items: center; gap: 8px; }
  .contact-line svg { width: 14px; height: 14px; }
  .contact-email { margin-top: 16px; }
  .address {
    position: absolute;
    left: 44px;
    bottom: 36px;
    color: var(--ink);
    font-size: 17px;
    line-height: 1.4;
  }
</style>
</head>
<body>

  <section class="card card-back" aria-label="Card back">
    <div class="wordmark"><span class="wordmark-mark"></span>Marlowe Building Co</div>
    <p class="tagline">New Homes, Additions &amp; Renovations<br>Residential &amp; Commercial Builders</p>
  </section>

  <section class="card card-front" aria-label="Card front">
    <svg class="front-wave" viewBox="0 0 660 377" preserveAspectRatio="none" aria-hidden="true">
      <defs>
        <linearGradient id="goldFill" x1="0" y1="0" x2="1" y2="1">
          <stop offset="0" stop-color="#e8a236"/>
          <stop offset="1" stop-color="#c98421"/>
        </linearGradient>
      </defs>
      <path d="M0 222 C 180 232, 300 170, 660 148 L660 377 L0 377 Z" fill="url(#goldFill)"/>
      <path d="M0 232 C 180 242, 310 180, 660 158" fill="none" stroke="#ffffff" stroke-width="5"/>
    </svg>

    <div class="wordmark front-wordmark"><span class="wordmark-mark"></span>Marlowe Building Co</div>

    <p class="reg">Reg# 38095</p>

    <div class="person">
      <p class="person-name">Daniel Ferris</p>
      <p class="person-role">director</p>
    </div>

    <div class="contacts">
      <p class="contact-line">08 9412 5586
        <svg viewBox="0 0 16 16" aria-label="phone"><path d="M4 1 L6.5 4 L5 6 C6 8.5 7.5 10 10 11 L12 9.5 L15 12 L13 15 C7 15 1 9 1 3 Z" fill="#1c1f26"/></svg>
      </p>
      <p class="contact-line">08 9412 5587
        <svg viewBox="0 0 16 16" aria-label="fax"><rect x="4" y="1" width="8" height="5" fill="#1c1f26"/><rect x="1" y="6" width="14" height="6" rx="1" fill="#1c1f26"/><rect x="4" y="11" width="8" height="4" fill="#1c1f26"/></svg>
      </p>
      <p class="contact-line">0412 558 903
        <svg viewBox="0 0 16 16" aria-label="mobile"><rect x="4" y="1" width="8" height="14" rx="1.5" fill="none" stroke="#1c1f26" stroke-width="1.6"/><circle cx="8" cy="12.5" r="0.9" fill="#1c1f26"/></svg>
      </p>
      <p class="contact-line">
        <svg viewBox="0 0 16 16" aria-label="email" style="margin-left:auto"><rect x="1" y="3" width="14" height="10" fill="#1c1f26"/><path d="M1 3 L8 9 L15 3" fill="none" stroke="#e39b2e" stroke-width="1.2"/></svg>
      </p>
      <p class="contact-email">marlowebuildingco@mail.com</p>
    </div>

    <address class="address" style="font-style:normal">
      24 Banksia Way<br>Kinross<br>WA 6028
    </address>
  </section>

</body>
</html>
```